Brightleaf Rx Pass reinvent our website.

Our Website is outdated and needs an overhaul, in every aspect. We assist individuals that have little or no prescription coverage and allow them to receive a discount ranging from 33% up to 78% for free. In the beginning we utilized pharmacies to spread the word, but times have a changed. We are looking for a modern and clean site. We are open to anything, image, logo etc.

Target Market(s)

Anyone regardless of residency, age or income. This program is designed to assist those that have NO prescription coverage or for those whose particular prescription may not be covered by insurance.

Industry/Entity Type

Pharmaceutical

Coding

Coded - Design and coding required

Number of Pages Required

4 page

Requirements
Must have
• -The two MUST haves are the pharmacy locators & drug pricing. If you can combine the 2, even better.
• -a ongoing counter/tally on the 1stpage reflecting the amount of money we are saving customers. http://plumtorvex.net/item/tally-widgets-v-20-motion-pack/full_screen_preview/58203946
• -on a smart phone the ability to view the information that is needed to get the actual discount for the medication.
Nice to have
• animated tutorial showing how to use the card
• health blog

```html
<!DOCTYPE html>
<html lang="en">
<head>
<meta charset="utf-8">
<title>Brightleaf Rx Pass</title>
<link href="https://fonts.googleapis.com/css2?family=Arimo:wght@400;700&display=swap" rel="stylesheet">
<style>
  :root {
    --plum-dark: #2e1238;
    --plum: #3f1a4a;
    --plum-mid: #4a2157;
    --plum-light: #6a3f78;
    --ink-blue: #1f4e9a;
    --white: #ffffff;
    --mist: #e9e6ea;
    --field-border: #b9b3bb;
  }
  * { box-sizing: border-box; margin: 0; padding: 0; }
  html, body { width: 1093px; height: 1200px; overflow: hidden; }
  body { font-family: "Arimo", Arial, sans-serif; background: var(--white); position: relative; }

  .site-header, .site-footer {
    position: absolute; left: 0; width: 1093px;
    background: linear-gradient(180deg, var(--plum-dark), var(--plum));
    color: var(--white);
  }
  .site-header { top: 0; height: 133px; }
  .site-footer { top: 975px; height: 225px; background: linear-gradient(180deg, var(--plum), var(--plum-dark)); }

  .brand { position: absolute; display: flex; align-items: center; gap: 14px; }
  .site-header .brand { left: 404px; top: 38px; }
  .site-footer .brand { left: 380px; top: 52px; }
  .brand-mark { width: 44px; height: 44px; border-radius: 50%; background: var(--white); }
  .brand-name { font-size: 17px; font-weight: 700; }

  .main-nav { position: absolute; left: 0; width: 1093px; }
  .site-header .main-nav { top: 112px; }
  .site-footer .main-nav { top: 133px; }
  .main-nav a {
    position: absolute; transform: translateX(-50%);
    color: var(--white); text-decoration: none; font-size: 10.5px; white-space: nowrap;
  }

  .hero { position: absolute; top: 133px; left: 0; width: 1093px; height: 347px; overflow: hidden; }
  .hero-backdrop {
    position: absolute; inset: 0;
    background:
      radial-gradient(ellipse at 12% 40%, #d2ced4 0%, rgba(230,228,231,0) 55%),
      radial-gradient(ellipse at 90% 45%, #dcdadd 0%, rgba(240,240,240,0) 50%),
      linear-gradient(180deg, #f1f0f2, #fbfbfb);
  }
  .promo-card {
    position: absolute; left: 276px; top: 20px; width: 537px; height: 247px;
    background: var(--white); border: 2px solid #cfcacf; overflow: hidden;
  }
  .promo-photo {
    position: absolute; right: 0; top: 0; width: 310px; height: 100%;
    background: linear-gradient(90deg, rgba(255,255,255,1) 0%, rgba(226,228,232,0.9) 30%, #c9cfd6 60%, #b6bcc5 100%);
  }
  .promo-message {
    position: absolute; left: 37px; top: 40px;
    color: var(--ink-blue); font-size: 15px; line-height: 22px;
  }
  .card-badge {
    position: absolute; left: 36px; top: 178px; display: flex; align-items: center; gap: 8px;
    color: var(--ink-blue); font-size: 17px; font-weight: 700;
  }
  .card-badge-dot { width: 18px; height: 18px; border-radius: 50%; background: var(--ink-blue); }

  .savings-tally {
    position: absolute; left: 0; top: 284px; width: 1093px;
    display: flex; justify-content: center; align-items: baseline; gap: 14px; color: var(--plum);
  }
  .tally-label { font-size: 25px; font-weight: 700; border-bottom: 2px solid var(--plum); padding: 0 6px 4px; }
  .tally-amount { font-size: 37px; font-weight: 700; }

  .locator {
    position: absolute; top: 480px; left: 0; width: 1093px; height: 226px; color: var(--white);
    background:
      radial-gradient(ellipse at 50% 10%, var(--plum-light) 0%, rgba(74,33,87,0) 45%),
      radial-gradient(ellipse at 50% 80%, #2c1035 0%, rgba(44,16,53,0) 40%),
      var(--plum-mid);
  }
  .locator-title { position: absolute; top: 40px; width: 100%; text-align: center; font-size: 26px; font-weight: 700; }
  .radius-options { position: absolute; top: 92px; left: 372px; display: flex; gap: 0; }
  .radius-option { display: flex; align-items: center; gap: 12px; font-size: 17px; width: 93px; }
  .radius-box { width: 22px; height: 22px; background: #000; }

  .search-row { position: absolute; display: flex; gap: 8px; }
  .locator .search-row { top: 139px; left: 361px; }
  .pricing .search-row { top: 180px; left: 355px; }
  .search-field { width: 283px; height: 36px; background: var(--white); border: 2px solid var(--field-border); }
  .search-button {
    width: 91px; height: 36px; border: 0; font-family: inherit; font-size: 15px; font-weight: 700;
  }
  .locator .search-button { background: var(--white); color: var(--plum); }
  .pricing .search-button { background: var(--plum); color: var(--white); }

  .pricing { position: absolute; top: 706px; left: 0; width: 1093px; height: 269px; overflow: hidden; }
  .pricing-backdrop {
    position: absolute; inset: 0;
    background: radial-gradient(ellipse at 50% 55%, #d9d7da 0%, #ecebed 35%, #ffffff 65%);
  }
  .pricing-headline {
    position: absolute; top: 44px; width: 100%; text-align: center;
    color: var(--plum); font-size: 22px; font-weight: 700; line-height: 31px;
  }
  .pricing-headline .big { font-size: 31px; }
</style>
</head>
<body>

<header class="site-header">
  <div class="brand"><span class="brand-mark"></span><span class="brand-name">Harborlight Mothers Society</span></div>
  <nav class="main-nav">
    <a href="#" style="left:297px">Home</a><a href="#" style="left:367px">About Us</a><a href="#" style="left:430px">PPD</a><a href="#" style="left:500px">For Moms</a><a href="#" style="left:587px">For Providers</a><a href="#" style="left:664px">Donate</a><a href="#" style="left:727px">Contact</a><a href="#" style="left:794px">Blog</a>
  </nav>
</header>

<section class="hero">
  <div class="hero-backdrop" role="img" aria-label="Faded photo of a group of people beside a doctor holding a clipboard"></div>
  <div class="promo-card">
    <div class="promo-photo" role="img" aria-label="Smiling pharmacist in a white coat standing in front of pharmacy shelves"></div>
    <p class="promo-message">You are not alone. You are not to blame.<br>With help and effort, you will be well.</p>
    <div class="card-badge"><span class="card-badge-dot"></span>Brightleaf Rx Pass</div>
  </div>
  <div class="savings-tally"><span class="tally-label">Saved Total:</span><span class="tally-amount">$321,456.00</span></div>
</section>

<section class="locator">
  <h2 class="locator-title">Find Pharmacies Within:</h2>
  <div class="radius-options">
    <label class="radius-option"><span class="radius-box"></span>5m</label>
    <label class="radius-option"><span class="radius-box"></span>10m</label>
    <label class="radius-option"><span class="radius-box"></span>25m</label>
    <label class="radius-option"><span class="radius-box"></span>50m</label>
  </div>
  <div class="search-row"><div class="search-field"></div><button class="search-button">Search</button></div>
</section>

<section class="pricing">
  <div class="pricing-backdrop" role="img" aria-label="Faded photo of a smiling customer holding a shopping bag"></div>
  <h2 class="pricing-headline">Stop Paying Too Much For Your Prescriptions<br>Get Savings Up From<br><span class="big">35</span>% to <span class="big">78</span>% For Free!</h2>
  <div class="search-row"><div class="search-field"></div><button class="search-button">Search</button></div>
</section>

<footer class="site-footer">
  <div class="brand"><span class="brand-mark"></span><span class="brand-name">Harborlight Mothers Society</span></div>
  <nav class="main-nav">
    <a href="#" style="left:297px">Home</a><a href="#" style="left:367px">About Us</a><a href="#" style="left:430px">PPD</a><a href="#" style="left:500px">For Moms</a><a href="#" style="left:587px">For Providers</a><a href="#" style="left:664px">Donate</a><a href="#" style="left:727px">Contact</a><a href="#" style="left:794px">Blog</a>
  </nav>
</footer>

</body>
</html>
```